Zielgruppe
Wir sind eine Weiterbildungsfirma mit der Zielgruppe Unternehmer, Selbstständige, Führungskräfte und Vertriebler.
Aufgabenstellung
Es soll dynamisch, elegant und professionell wirken. Der Titel muss gut lesbar sein.
(Wir haben einen Pixmora-Foto-Account auf Abo-Basis.)
Der Titel lautet neu: Die Kelbing-Prinzipien für echte Durchbrüche

```html
<!DOCTYPE html>
<html lang="de">
<head>
<meta charset="utf-8">
<title>Die Kelbing-Prinzipien für echte Durchbrüche – Buchcover</title>
<link rel="stylesheet" href="https://fonts.googleapis.com/css2?family=Fira+Sans:wght@500;600&display=swap">
<style>
  :root {
    --cover-bg: #f6f6f6;
    --title-red: #d0505b;
    --band-black: #222222;
    --band-text: #ffffff;
  }
  * { margin: 0; padding: 0; box-sizing: border-box; }
  html, body {
    width: 864px;
    height: 1200px;
    overflow: hidden;
    background: var(--cover-bg);
  }
  .book-cover {
    position: relative;
    width: 864px;
    height: 1200px;
    background: var(--cover-bg);
    font-family: "Fira Sans", sans-serif;
    overflow: hidden;
  }
  .publisher-mark {
    position: absolute;
    top: 70px;
    right: 56px;
    display: flex;
    align-items: center;
    gap: 10px;
    color: var(--title-red);
    font-weight: 600;
    font-size: 17px;
    letter-spacing: 0.02em;
    text-transform: uppercase;
  }
  .publisher-mark .mark-square {
    width: 34px;
    height: 34px;
    background: var(--title-red);
  }
  .publisher-mark .mark-name {
    line-height: 1.1;
    width: 110px;
  }
  .cover-title {
    position: absolute;
    left: 0;
    top: 150px;
    color: var(--title-red);
    font-weight: 600;
    font-size: 122px;
    line-height: 150px;
    letter-spacing: -0.01em;
  }
  .cover-title .title-line { display: block; white-space: nowrap; }
  .cover-title .title-highlight {
    display: inline-block;
    margin-top: 20px;
    padding: 0 22px 6px 8px;
    background: var(--band-black);
    color: var(--band-text);
    line-height: 150px;
  }
</style>
</head>
<body>
  <main class="book-cover">
    <div class="publisher-mark">
      <span class="mark-square"></span>
      <span class="mark-name">Jonas Kelbing Institut</span>
    </div>
    <h1 class="cover-title">
      <span class="title-line">Die</span>
      <span class="title-line">Kelbing-</span>
      <span class="title-line">Prinzipien</span>
      <span class="title-line">für echte</span>
      <span class="title-line"><span class="title-highlight">Durchbrüche</span></span>
    </h1>
  </main>
</body>
</html>
```